The Copper Ladder

we require a classy business card design for a business coaching company that uses our current logo and the wording:

Front of card:

LOGO
Kyle Morrison
CEO
TEL: 1300 4 52918
FAX: 1300 5 52918
Mobile: 0412 638194
PO Box 917, Ferris Hollow, Brisbane, Qld 4127
e: kylem@copperladder.com.au
w: www.copperladder.com.au

Reverse side of the card:

Systematizing Businesses into Turnkey Operations
Strategic Business Plans
Sales & Marketing Programs
Sales Training & Business Coaching
Internet Marketing & Web Design

Here’s what our clients say:

“We grew from $396,000 to over $5million in 4 years and made KTS’s Rising Enterprises Roll 3 years running!” – Martin Greaves, Meridian Works

Target Market(s)

small to medium sized business owners in Australia

Industry/Entity Type

Business

Requirements
Must have
• standard business card size

```html
<!DOCTYPE html>
<html lang="en">
<head>
<meta charset="utf-8">
<title>The Copper Ladder – Business Card</title>
<link href="https://fonts.googleapis.com/css2?family=EB+Garamond:ital,wght@0,400;0,500;0,600;1,400&display=swap" rel="stylesheet">
<style>
  :root {
    --page: #fdf3e0;
    --card: #000000;
    --ink: #ffffff;
    --gold: #f5a81c;
    --shadow: rgba(40, 30, 10, 0.45);
  }
  * { box-sizing: border-box; margin: 0; padding: 0; }
  html, body { width: 928px; height: 1200px; overflow: hidden; }
  body {
    background: var(--page);
    font-family: "EB Garamond", Georgia, serif;
    color: var(--ink);
    position: relative;
  }
  .card {
    position: absolute;
    left: 189px;
    width: 550px;
    height: 370px;
    background: var(--card);
    box-shadow: 6px 12px 14px var(--shadow);
  }
  .card--front { top: 150px; }
  .card--back { top: 700px; }

  /* Front */
  .brand {
    position: absolute;
    top: 34px; left: 0; right: 0;
    text-align: center;
    font-size: 52px;
    font-weight: 500;
    letter-spacing: 0.5px;
    line-height: 1;
  }
  .tagline {
    position: absolute;
    top: 118px; left: 0; right: 0;
    text-align: center;
    font-style: italic;
    font-size: 21px;
    line-height: 1.15;
  }
  .rule {
    position: absolute;
    height: 1px;
    background: var(--gold);
  }
  .rule--left { top: 164px; left: 26px; width: 100px; }
  .rule--right { top: 142px; right: 26px; width: 100px; }
  .person {
    position: absolute;
    top: 196px; left: 0; right: 0;
    text-align: center;
    line-height: 1.05;
  }
  .person__name { font-size: 36px; font-weight: 600; letter-spacing: 0.5px; }
  .person__title { font-size: 26px; font-weight: 500; }
  .phones {
    position: absolute;
    left: 24px; bottom: 20px;
    font-size: 12.5px;
    line-height: 1.3;
  }
  .address {
    position: absolute;
    right: 20px; top: 262px;
    font-size: 12.5px;
    line-height: 1.3;
  }
  .website {
    position: absolute;
    left: 168px; bottom: 22px;
    font-size: 20px;
    font-weight: 600;
    letter-spacing: 0.5px;
  }

  /* Back */
  .services {
    list-style: none;
    position: absolute;
    top: 26px; left: 18px;
  }
  .services li {
    display: flex;
    align-items: center;
    font-size: 23px;
    line-height: 30px;
    white-space: nowrap;
  }
  .services svg { width: 30px; height: 26px; margin-right: 10px; flex: none; }
  .rule--back { top: 196px; left: 0; width: 100%; }
  .testimonial {
    position: absolute;
    top: 222px; left: 0; right: 0;
    text-align: center;
    font-size: 15.5px;
    line-height: 1.35;
  }
  .testimonial__intro { margin-bottom: 20px; }
  .testimonial__quote { margin-bottom: 18px; }
  .testimonial__source { padding-left: 60px; }
</style>
</head>
<body>

<section class="card card--front" aria-label="Business card front">
  <div class="brand">The Copper Ladder</div>
  <p class="tagline">marketing that’s so effective<br>it’s like printing your own money</p>
  <span class="rule rule--left"></span>
  <span class="rule rule--right"></span>
  <div class="person">
    <div class="person__name">Kyle Morrison</div>
    <div class="person__title">CEO</div>
  </div>
  <div class="phones">
    TEL: 1300 4 52918<br>
    FAX: 1300 5 52918<br>
    Mobile: 0412 638194
  </div>
  <div class="address">
    PO Box 917<br>
    Ferris Hollow, Brisbane, Qld 4127<br>
    e: kylem@copperladder.com.au
  </div>
  <div class="website">www.copperladder.com.au</div>
</section>

<section class="card card--back" aria-label="Business card back">
  <svg width="0" height="0" style="position:absolute">
    <symbol id="tick" viewBox="0 0 30 26">
      <path d="M2 14 L7 11 L11 18 Q18 6 29 1 Q19 10 12 25 Z" fill="var(--gold)"/>
    </symbol>
  </svg>
  <ul class="services">
    <li><svg><use href="#tick"/></svg>Systematizing Businesses into Turnkey Operations</li>
    <li><svg><use href="#tick"/></svg>Strategic Business Plans</li>
    <li><svg><use href="#tick"/></svg>Sales &amp; Marketing Programs</li>
    <li><svg><use href="#tick"/></svg>Sales Training &amp; Business Coaching</li>
    <li><svg><use href="#tick"/></svg>Internet Marketing &amp; Web Design</li>
  </ul>
  <span class="rule rule--back"></span>
  <div class="testimonial">
    <p class="testimonial__intro">Here’s what our clients say:</p>
    <p class="testimonial__quote">“We grew from $396,000 to over $5 million in 4 years and made<br>KTS’s Rising Enterprises Roll 3 years running!”</p>
    <p class="testimonial__source">– Martin Greaves, Meridian Works</p>
  </div>
</section>

</body>
</html>
```